Memoir author looking for book cover design

Title:
"Rain, Rust and Return"

Subtitle:
"A Season Spent Chasing Our Father Across the Coastline"

My book is about the 18-month-long search and grieving process after my husband went missing from a hiking accident.
See "notesbeyondthequietharbor.example" for background

(An "ampersand" may look best, but I'm unable to enter it in this format)

Reason: Having difficulty finishing up, in part due to time difference. Don't want designers to have to work in the middle of the night!

```html
<!DOCTYPE html>
<html lang="en">
<head>
<meta charset="UTF-8">
<title>Rain, Rust and Return – Book Cover</title>
<link href="https://fonts.googleapis.com/css2?family=Anton&family=Montserrat:wght@400;500&display=swap" rel="stylesheet">
<style>
  :root {
    --paper: #f3f3f1;
    --paper-edge: #e6e6e3;
    --ink: #1d1d1b;
    --sky: #8eafd3;
    --haze: #a7b9c9;
    --forest: #4e6b46;
    --shade: #2f3a2b;
    --rock: #27261f;
  }
  html, body {
    margin: 0;
    padding: 0;
    overflow: hidden;
    background: var(--paper);
  }
  .cover {
    position: relative;
    width: 821px;
    height: 1200px;
    overflow: hidden;
    background: radial-gradient(ellipse at 50% 45%, #fafaf8 0%, var(--paper) 60%, var(--paper-edge) 100%);
  }
  .cover-title {
    position: absolute;
    left: 0;
    top: 0;
    width: 821px;
    height: 860px;
  }
  .cover-title text {
    font-family: "Anton", "Oswald", sans-serif;
  }
  .title-line-1 { font-size: 336px; }
  .title-line-2 { font-size: 318px; }
  .title-line-3 { font-size: 190px; }
  .cover-subtitle {
    position: absolute;
    left: 0;
    top: 878px;
    width: 821px;
    margin: 0;
    text-align: center;
    font-family: "Montserrat", sans-serif;
    font-weight: 400;
    font-size: 29px;
    line-height: 52px;
    letter-spacing: 0.01em;
    text-transform: uppercase;
    color: var(--ink);
  }
  .cover-author {
    position: absolute;
    left: 0;
    top: 1082px;
    width: 821px;
    margin: 0;
    text-align: center;
    font-family: "Montserrat", sans-serif;
    font-weight: 400;
    font-size: 60px;
    line-height: 80px;
    letter-spacing: 0.2em;
    text-indent: 0.2em;
    text-transform: uppercase;
    color: var(--ink);
  }
</style>
</head>
<body>
<main class="cover">
  <svg class="cover-title" viewBox="0 0 821 860" role="img"
       aria-label="Title lettering filled with a hiking photograph: a man in a kilt with a backpack standing on a rocky outcrop above a hazy forested valley">
    <defs>
      <linearGradient id="landscape-fill" gradientUnits="userSpaceOnUse" x1="0" y1="86" x2="0" y2="838">
        <stop offset="0" stop-color="var(--sky)"/>
        <stop offset="0.3" stop-color="var(--haze)"/>
        <stop offset="0.48" stop-color="#6f8a72"/>
        <stop offset="0.62" stop-color="var(--forest)"/>
        <stop offset="0.8" stop-color="var(--shade)"/>
        <stop offset="1" stop-color="var(--rock)"/>
      </linearGradient>
      <filter id="letter-lift" x="-5%" y="-5%" width="110%" height="110%">
        <feDropShadow dx="0" dy="1.5" stdDeviation="1.5" flood-color="#000" flood-opacity="0.16"/>
      </filter>
    </defs>
    <g fill="url(#landscape-fill)" filter="url(#letter-lift)" text-anchor="start">
      <text class="title-line-1" x="86" y="376" textLength="646" lengthAdjust="spacingAndGlyphs">RAIN</text>
      <text class="title-line-2" x="86" y="656" textLength="646" lengthAdjust="spacingAndGlyphs">RUST</text>
      <text class="title-line-3" x="84" y="838" textLength="650" lengthAdjust="spacingAndGlyphs">&amp; RETURN</text>
    </g>
  </svg>

  <p class="cover-subtitle">A Season Spent Chasing Our<br>Father Across the Coastline</p>

  <p class="cover-author">Author Name</p>
</main>
</body>
</html>
```